New profile page for existing party website

For the party website 'Brindlepost' we need a new design for the user profile page.

The page should show
* a profile picture
* basic information like name, age and city
* music styles he/she likes
* links to their Facebook profile and website
* a bio (HTML content)
* events they plan to go to
* past events
* pictures

Challenge is that some users may have little information (just their name) while others have a huge description, lots of foto's, events, etc.

Please visit http://www.brindlepost.example and http://www.brindlepost.example/users/tobias

Target Market(s)

Men and women between 18 and 35

Industry/Entity Type

Night Club

Number of Pages Required

2 page

Font styles to use
Other font styles liked:
• Roboto

Requirements
Must have
• Please design how the page looks with a fully filled out profile and with an empty profile.
• It should fit well with the existing website.
• Include designs for both for small screens (mobile) and large screens (tablet, desktop).
Nice to have
• UX design on how to collapse or paginate sections.
• Interactive effects would be a bonus.
Should not have
• The page should not have subnavigation like menus or tabs.

```html
<!DOCTYPE html>
<html lang="nl">
<head>
<meta charset="utf-8">
<title>Brindlepost – Profiel</title>
<link rel="stylesheet" href="https://fonts.googleapis.com/css2?family=Raleway:wght@400;500;600&family=Open+Sans:wght@400;600;700&display=swap">
<style>
:root{
  --black:#050505;
  --footer:#141414;
  --band:#2d2d2d;
  --white:#ffffff;
  --ink:#222222;
  --body:#6a6a6a;
  --rule:#d8d8d8;
  --orange:#f29a26;
  --hero-a:#5a1e1e;
  --hero-b:#2a2a30;
}
*{box-sizing:border-box;margin:0;padding:0}
html,body{width:1200px;height:2490px;overflow:hidden;background:var(--white)}
body{position:relative;font-family:"Open Sans",Arial,sans-serif;color:var(--body)}

/* header */
.site-header{position:absolute;left:0;top:0;width:1200px;height:121px;background:var(--black)}
.brand{position:absolute;left:93px;top:38px;display:flex;align-items:center;gap:12px;color:var(--white);font-family:"Raleway",sans-serif;font-weight:600;font-size:34px}
.brand-dot{width:18px;height:18px;border-radius:50%;background:var(--white)}
.main-nav{position:absolute;left:380px;top:52px;display:flex;gap:26px;font-family:"Raleway",sans-serif;font-size:18px;color:var(--white)}
.search{position:absolute;left:812px;top:45px;width:166px;height:35px;background:#ececec;color:#9a9a9a;font-size:14px;padding:8px 14px}
.account-btn{position:absolute;left:988px;top:45px;width:109px;height:35px;border:2px solid var(--white);color:var(--white);font-family:"Raleway",sans-serif;font-weight:600;font-size:14px;text-align:center;line-height:31px}

/* hero */
.profile-hero{position:absolute;left:0;top:121px;width:1200px;height:394px;background:linear-gradient(100deg,var(--hero-a),#3c2424 35%,var(--hero-b) 70%,#4a1e22)}
.hero-arrow{position:absolute;top:178px}
.avatar{position:absolute;left:517px;top:20px;width:166px;height:166px;border-radius:50%;border:4px solid var(--white);background:radial-gradient(circle at 50% 40%,#b79a86,#5b4434)}
.profile-name{position:absolute;left:0;top:218px;width:1200px;text-align:center;font-family:"Raleway",sans-serif;font-size:30px;font-weight:500;color:var(--white);letter-spacing:1px}
.profile-meta{position:absolute;left:0;width:1200px;text-align:center;font-size:13px;font-weight:700;color:var(--white);text-transform:uppercase}
.profile-meta.first{top:270px}
.profile-meta.second{top:302px}
.meta-sep{margin:0 14px}
.socials{position:absolute;left:570px;top:336px;display:flex;gap:6px}
.social-link{width:28px;height:28px;border-radius:50%;background:var(--white);display:flex;align-items:center;justify-content:center}

/* bio */
.bio{position:absolute;left:96px;top:0;width:1000px}
.bio h2{font-family:"Raleway",sans-serif;font-weight:400;font-size:27px;color:var(--ink);margin-bottom:14px}
.bio p{font-size:14px;line-height:24px}
.rule{position:absolute;left:103px;width:997px;height:2px;background:var(--rule)}
.conditions{list-style:none}
.conditions li{font-size:14px;line-height:33px;padding-left:20px;position:relative}
.conditions li::before{content:"";position:absolute;left:2px;top:13px;width:7px;height:7px;border-right:1.5px solid #888;border-bottom:1.5px solid #888;transform:rotate(-45deg)}

/* plan band */
.plan-band{position:absolute;left:0;top:1499px;width:1200px;height:452px;background:var(--band)}
.band-title{position:absolute;left:105px;top:55px;font-family:"Raleway",sans-serif;font-weight:400;font-size:30px;color:var(--white)}
.band-arrow{position:absolute;top:70px;width:30px;height:30px;border-radius:50%;background:#151515}
.event-card{position:absolute;top:119px;width:234px}
.event-poster{width:234px;height:167px;border:3px solid var(--white)}
.event-title{margin-top:14px;font-family:"Raleway",sans-serif;font-size:21px;font-weight:500;color:var(--orange)}
.event-text{margin-top:4px;font-size:13px;line-height:18px;color:#d2d2d2}

/* lower */
.section-title{position:absolute;top:1988px;font-family:"Raleway",sans-serif;font-weight:400;font-size:31px;color:var(--orange)}
.past-event{position:absolute;width:250px}
.past-event .name{font-size:15px;color:var(--ink);text-transform:uppercase}
.past-event .city{font-size:13px;color:var(--body);margin-top:1px}
.past-event .date{font-size:13px;color:var(--orange);margin-top:1px}
.more-btn{position:absolute;left:374px;top:2251px;width:129px;height:40px;background:var(--orange);color:var(--white);font-size:14px;font-weight:700;text-align:center;line-height:40px}
.thumb{position:absolute;width:148px;height:125px;border:3px solid #f0f0f0;box-shadow:0 0 0 1px #dcdcdc}

/* footer */
.site-footer{position:absolute;left:0;top:2357px;width:1200px;height:133px;background:var(--footer);text-align:center}
.footer-links{margin-top:34px;display:flex;justify-content:center;gap:34px;font-family:"Raleway",sans-serif;font-size:16px;color:var(--white)}
.copyright{margin-top:10px;font-size:12px;color:#8a8a8a}
</style>
</head>
<body>

<header class="site-header">
  <div class="brand"><span class="brand-dot"></span>Brindlepost</div>
  <nav class="main-nav"><span>Home</span><span>Agenda</span><span>Free tickets</span><span>Photos</span><span>News</span></nav>
  <div class="search">Zoeken</div>
  <div class="account-btn">My Account</div>
</header>

<section class="profile-hero" role="img" aria-label="Blurred party crowd background">
  <svg class="hero-arrow" style="left:54px" width="20" height="36" viewBox="0 0 20 36"><path d="M18 2 2 18l16 16" fill="none" stroke="#ffffff" stroke-opacity=".5" stroke-width="2"/></svg>
  <svg class="hero-arrow" style="left:1126px" width="20" height="36" viewBox="0 0 20 36"><path d="M2 2l16 16L2 34" fill="none" stroke="#ffffff" stroke-opacity=".5" stroke-width="2"/></svg>
  <div class="avatar" role="img" aria-label="Profile photo"></div>
  <h1 class="profile-name">JORISV PHOTOGRAPHY</h1>
  <p class="profile-meta first">Member since : January 1, 2006<span class="meta-sep">/</span>Age : 34<span class="meta-sep">/</span>City : Amersfoort<span class="meta-sep">/</span>Music : Latin<span class="meta-sep">/</span>Salsa</p>
  <p class="profile-meta second">Active since: Jan 2006 &nbsp;&nbsp; Shoots: 500 and counting</p>
  <div class="socials">
    <span class="social-link" aria-label="Profile link">
      <svg width="16" height="16" viewBox="0 0 16 16"><path d="M6.5 9.5l3-3M7 4.5l1.2-1.2a2.5 2.5 0 013.5 3.5L10.5 8M9 11.5l-1.2 1.2a2.5 2.5 0 01-3.5-3.5L5.5 8" fill="none" stroke="#111" stroke-width="1.6" stroke-linecap="round"/></svg>
    </span>
    <span class="social-link" aria-label="Website">
      <svg width="16" height="16" viewBox="0 0 16 16"><circle cx="8" cy="8" r="6" fill="none" stroke="#111" stroke-width="1.4"/><path d="M2 8h12M8 2c2 2 2 10 0 12M8 2c-2 2-2 10 0 12" fill="none" stroke="#111" stroke-width="1.2"/></svg>
    </span>
  </div>
</section>

<article class="bio" style="top:576px">
  <h2>Wil jij fotograferen voor Brindlepost?</h2>
  <p>Als je uitgaan leuk vindt, makkelijk bent in de omgang en uiteraard houdt van fotograferen, biedt Brindlepost je de kans een kijkje te nemen in de wereld van de partyfotografie. Door de inzet van de fotografen is Brindlepost uitgegroeid tot een van de meest toonaangevende partysites van Nederland. De betrouwbaarheid, de hoge kwaliteit van de foto's en het coveren van de belangrijkste evenementen maakt van Brindlepost een van de best bezochte websites in ons vakgebied</p>
</article>
<div class="rule" style="top:743px"></div>

<article class="bio" style="top:780px">
  <h2>Belangrijk informatie</h2>
  <p>Fotograferen voor Brindlepost is op vrijwillige basis. Je kan kiezen waar en wanneer je uitgaat en foto's maakt, maar een vaste inbreng word wel van je verwacht. Hoe meer je voor Brindlepost doet, hoe meer ervaring je opdoet met de camera en hoe beter je word. Hierdoor kan je weer naar interessantere feesten en festivals. Wat je wel krijgt is gratis entree voor een evenement en soms ook andere voordelen zoals gratis drankjes... Je gaat meestal met ze tweetjes op pad en ontmoet veel nieuwe mensen zoals DJ's en organisatoren. Hoe meer je voor Brindlepost.nl werkt hoe meer ervaring je er ook uit zal halen. De beste fotografen doen de leukste en de meest uitdagende evenementen bijvoorbeeld: Galaxia, Vortex Outdoor, Helios Weekend, Shore Dance etc.</p>
</article>
<div class="rule" style="top:998px"></div>

<article class="bio" style="top:1024px">
  <h2 style="margin-bottom:6px">Voorwaarden</h2>
  <ul class="conditions">
    <li>Je moet 18 jaar of ouder zijn.</li>
    <li>Je moet het aankunnen om hoge kwaliteit foto's te maken en professioneel gedrag vertonen.</li>
    <li>Je moet sociaal zijn; een open persoon zijn die ervan houdt om ander e mensen te ontmoeten.</li>
    <li>Het is een vereiste dat je een digitale spiegelreflex-camera hebt en lichtsterke lens met vast diafragma van F2.8 en natuurlijk een externe flitser (E-TTL).</li>
    <li>Je bent verantwoordelijk voor je eigen vervoer om naar de evenementen te gaan waar je foto's maakt.</li>
  </ul>
</article>
<div class="rule" style="top:1256px"></div>

<article class="bio" style="top:1282px">
  <h2 style="margin-bottom:8px">Aanmelden</h2>
  <p>Wil jij ook het team van Brindlepost versterken en het nachtleven van een andere kant verkennen? Geef je dan op, stuur een mailtje naar joris@brindlepost.example Vermeld daar goed in je naam, leeftijd, woonplaats en het type camera dat je hebt en je ervaring op het gebied van fotograferen.</p>
  <p style="margin-top:8px">Bekijk ons online foto album voor de door mij geschoten foto's. Bekijk al mijn videofilmpjes via mijn eigen videokanaal</p>
  <p style="margin-top:8px">www.videohub.example/user/1982JorisV</p>
</article>

<section class="plan-band">
  <h2 class="band-title">Event Plan to Go</h2>
  <svg class="band-arrow" style="left:1026px" viewBox="0 0 30 30"><path d="M17 10l-5 5 5 5" fill="none" stroke="#fff" stroke-width="1.5"/></svg>
  <svg class="band-arrow" style="left:1067px" viewBox="0 0 30 30"><path d="M13 10l5 5-5 5" fill="none" stroke="#fff" stroke-width="1.5"/></svg>
  <div class="event-card" style="left:103px">
    <div class="event-poster" role="img" aria-label="Colourful festival poster" style="background:linear-gradient(160deg,#3aa34a,#d8472c)"></div>
    <h3 class="event-title">Sis parturient mont</h3>
    <p class="event-text">nascetur ridiculus mus in iaculis facilisis massa Etiam eu urna Sed porta Suspendisse quam leo</p>
  </div>
  <div class="event-card" style="left:357px">
    <div class="event-poster" role="img" aria-label="Mint green festival poster" style="background:linear-gradient(160deg,#a8dcc3,#7cc4a6)"></div>
    <h3 class="event-title">Phasellus pellent</h3>
    <p class="event-text">nascetur ridiculus mus in iaculis facilisis massa Etiam eu urna Sed porta Suspendisse quam leo</p>
  </div>
  <div class="event-card" style="left:611px">
    <div class="event-poster" role="img" aria-label="Yellow festival artwork" style="background:linear-gradient(160deg,#f7dc3a,#e8b80e)"></div>
    <h3 class="event-title">Sed porta Suspendisse</h3>
    <p class="event-text">nascetur ridiculus mus in iaculis facilisis massa Etiam eu urna Sed porta Suspendisse quam leo</p>
  </div>
  <div class="event-card" style="left:865px">
    <div class="event-poster" role="img" aria-label="Tropical festival poster" style="background:linear-gradient(170deg,#f4d22a,#2a9ad0 55%,#2f7a3a)"></div>
    <h3 class="event-title">Cras a ante vitae</h3>
    <p class="event-text">nascetur ridiculus mus in iaculis facilisis massa Etiam eu urna Sed porta Suspendisse quam leo</p>
  </div>
</section>

<h2 class="section-title" style="left:98px">Past Events</h2>
<div class="past-event" style="left:100px;top:2056px"><div class="name">Festival sol nuevo 2016</div><div class="city">Rotterdam</div><div class="date">25 March 2016</div></div>
<div class="past-event" style="left:100px;top:2139px"><div class="name">Rhoncus dictum 2016</div><div class="city">Rotterdam</div><div class="date">23 March 2016</div></div>
<div class="past-event" style="left:100px;top:2228px"><div class="name">Cras a ante vitae enim o 2016</div><div class="city">Rotterdam</div><div class="date">22 March 2016</div></div>
<div class="past-event" style="left:374px;top:2056px"><div class="name">Donec convallis 2016</div><div class="city">Rotterdam</div><div class="date">15 March 2016</div></div>
<div class="past-event" style="left:374px;top:2139px"><div class="name">Aliquam erat volutpa 2016</div><div class="city">Rotterdam</div><div class="date">10 March 2016</div></div>
<div class="more-btn">VIEW MORE</div>

<h2 class="section-title" style="left:632px">Photos</h2>
<div class="thumb" role="img" aria-label="Party photo" style="left:633px;top:2040px;background:linear-gradient(150deg,#9a8a74,#d66a22)"></div>
<div class="thumb" role="img" aria-label="Party photo" style="left:790px;top:2040px;background:linear-gradient(150deg,#b9b2a4,#e07a2a)"></div>
<div class="thumb" role="img" aria-label="Party photo" style="left:948px;top:2040px;background:linear-gradient(150deg,#7b6a58,#e2762a)"></div>
<div class="thumb" role="img" aria-label="Party photo" style="left:633px;top:2180px;background:linear-gradient(150deg,#8fae5c,#6a4a36)"></div>
<div class="thumb" role="img" aria-label="Party photo" style="left:790px;top:2180px;background:linear-gradient(150deg,#3a3030,#7a5a48)"></div>
<div class="thumb" role="img" aria-label="Party photo" style="left:948px;top:2180px;background:linear-gradient(150deg,#b7c4c8,#e2762a)"></div>

<footer class="site-footer">
  <nav class="footer-links"><span>CONTACT</span><span>TERMS OF USE</span><span>PRIVACY POLICY</span></nav>
  <p class="copyright">© 2016 Company Name &nbsp;All right reserved</p>
</footer>

</body>
</html>
```